Facebook Header Design Project.

I'm supplying white and colored logos. The Facebook page already exists. URL = https://www.pagebook.example/lumocrest.design The design should not be based on what's already there. Consider mobile implications of the design. This Design will form the designs of other social media headers. LumoCrest is a web design | digital marketing company.

Target Market(s)

People interested in web design | digital marketing services.

Industry/Entity Type

LumoCrest is a web design | digital marketing company. That should be clear in the design.

Colors
0054AA
0677BA
7BADD7
CADEEF
E8F1F8

Requirements
Must have
• Logo. Use Facebook header image dimension.
Nice to have
• Use a color scheme like the logo and feel free to add a color or two from the other side of the color whee.

```html
<!DOCTYPE html>
<html lang="en">
<head>
<meta charset="utf-8">
<title>LumoCrest – Page Header</title>
<link rel="stylesheet" href="https://fonts.googleapis.com/css2?family=Roboto:wght@400;500;700&family=Roboto+Condensed:ital,wght@1,600;1,700&display=swap">
<style>
:root{
  --brand-deep:#0054AA;
  --brand-mid:#0677BA;
  --brand-soft:#7BADD7;
  --brand-pale:#CADEEF;
  --brand-mist:#E8F1F8;
  --wave-start:#0E77C8;
  --wave-end:#3CE6F2;
  --ink:#1c1e21;
  --muted:#65676b;
  --link:#2d6fdc;
  --action:#4a72e8;
  --surface:#ffffff;
  --feed:#f0f2f5;
  --chip:#e4e6eb;
  --open:#45a843;
}
*{box-sizing:border-box;margin:0;padding:0}
html,body{width:1200px;height:1200px;overflow:hidden}
body{background:linear-gradient(135deg,#9a9b9e,#c4c5c8);font-family:"Roboto",sans-serif;color:var(--ink);position:relative}
.page{position:absolute;left:104px;top:53px;width:992px;height:1089px;background:var(--feed);overflow:hidden}
.abs{position:absolute}

/* cover */
.cover{left:0;top:0;width:992px;height:364px;background:var(--surface);overflow:hidden}
.cover-wave{left:0;top:160px;width:680px;height:204px;border-radius:0 110px 0 0;
  background:linear-gradient(90deg,var(--wave-start),var(--wave-end))}
.cover-illustration{left:60px;top:55px;width:390px;height:260px;border-radius:14px;
  background:linear-gradient(160deg,var(--brand-mist),var(--brand-pale) 55%,var(--brand-soft));opacity:.9}
.cover-dots-top{left:0;top:0;width:100px;height:100px;background:var(--brand-soft);opacity:.35;clip-path:polygon(0 0,100% 0,0 100%)}
.cover-dots-bottom{right:0;bottom:0;width:100px;height:100px;background:var(--brand-soft);opacity:.35;clip-path:polygon(100% 0,100% 100%,0 100%)}
.cover-brand{left:620px;top:92px;display:flex;align-items:center;gap:12px}
.cover-brand .mark{width:26px;height:26px;background:var(--brand-deep)}
.cover-brand .name{font-weight:700;font-size:46px;color:var(--brand-deep);letter-spacing:-.5px}
.services{left:620px;top:190px;list-style:none}
.services li{font-family:"Roboto Condensed",sans-serif;font-style:italic;font-weight:600;font-size:17px;color:var(--brand-deep);height:27px;display:flex;align-items:center}
.services li::before{content:"";width:9px;height:9px;background:var(--brand-mid);margin-right:13px}

/* identity strip */
.identity{left:0;top:364px;width:992px;height:162px;background:var(--surface)}
.avatar{left:25px;top:-12px;width:116px;height:116px;border-radius:50%;background:var(--surface);border:3px solid var(--brand-mid);display:flex;align-items:center;justify-content:center}
.avatar span{font-weight:700;font-size:17px;color:var(--brand-mid)}
.page-name{left:155px;top:40px;font-size:23px;font-weight:700}
.page-handle{left:155px;top:72px;font-size:13.5px;color:var(--muted)}
.call-btn{left:717px;top:58px;width:247px;height:33px;border-radius:4px;background:var(--action);color:#fff;font-weight:500;font-size:14px;display:flex;align-items:center;justify-content:center;gap:6px}
.divider{left:25px;top:114px;width:939px;height:1px;background:#ccd0d5}
.tabs{left:25px;top:124px;display:flex;font-size:12.5px;color:var(--muted)}
.tabs a{display:block;padding:0 13px;height:38px;line-height:26px;text-decoration:none;color:inherit}
.tabs a.active{color:var(--link);border-bottom:3px solid var(--link)}
.tabs .caret{display:inline-block;border:4px solid transparent;border-top-color:var(--muted);margin-left:5px;transform:translateY(2px)}
.page-btn{top:124px;height:28px;border-radius:4px;background:var(--chip);display:flex;align-items:center;justify-content:center;gap:5px;font-size:12.5px;font-weight:500;color:var(--ink)}
.btn-like{left:684px;width:101px;background:var(--brand-mist);color:var(--link)}
.btn-message{left:792px;width:82px}
.btn-search{left:882px;width:37px}
.btn-more{left:926px;width:38px}
.dot-icon{width:13px;height:13px;border-radius:50%;background:var(--ink)}

/* cards */
.card{background:var(--surface);border-radius:6px;box-shadow:0 1px 2px rgba(0,0,0,.15)}
.card h2{font-size:16px;font-weight:700}
.see-all{position:absolute;right:13px;top:18px;font-size:12px;color:var(--link)}
.about{left:24px;top:537px;width:389px;height:343px;padding:14px 13px}
.about-list{list-style:none;margin-top:14px}
.about-list li{display:flex;gap:10px;font-size:11.3px;line-height:15.5px;margin-bottom:13px;color:var(--ink)}
.about-list li .ico{flex:0 0 15px;height:15px;display:flex;align-items:center;justify-content:center}
.about-list .desc{max-width:318px}
.about-list .lnk{color:var(--link)}
.about-list .open{color:var(--open)}
.suggest{left:24px;top:892px;width:389px;height:152px;padding:14px 13px}
.suggest p{font-size:12.5px;color:#444;margin-top:10px}
.suggest .field{margin-top:10px;height:34px;border-radius:6px;background:var(--feed);font-size:13px;padding:0 10px;line-height:34px}
.suggest .choices{display:flex;gap:7px;margin-top:12px}
.suggest .choices span{flex:1;height:28px;border-radius:4px;background:var(--chip);font-size:12px;text-align:center;line-height:28px}
.photos{left:24px;top:1057px;width:389px;height:60px;padding:14px 13px}

.composer{left:425px;top:537px;width:539px;height:92px}
.composer .me{left:10px;top:9px;width:32px;height:32px;border-radius:50%;background:linear-gradient(135deg,#8a9688,#d2d9d0)}
.composer .me::after{content:"";position:absolute;right:0;bottom:0;width:8px;height:8px;border-radius:50%;background:var(--open);border:1.5px solid #fff}
.composer .field{left:50px;top:9px;width:479px;height:32px;border-radius:4px;background:var(--chip);font-size:14px;text-align:center;line-height:32px}
.composer .tools{left:0;top:56px;width:539px;display:flex;justify-content:space-around;font-size:12px;color:var(--muted)}
.composer .tools span{display:flex;align-items:center;gap:7px}

.post{left:425px;top:643px;width:539px;height:434px;overflow:hidden}
.post .author-mark{left:12px;top:10px;width:32px;height:32px;border-radius:50%;border:1.5px solid var(--brand-mid)}
.post .headline{left:51px;top:11px;font-size:11.5px;color:var(--muted)}
.post .headline b{color:var(--ink);font-weight:500}
.post .time{left:51px;top:27px;font-size:10.5px;color:var(--muted)}
.post .menu{right:14px;top:12px;font-size:14px;color:var(--muted);letter-spacing:1px}
.post-photo{left:0;top:47px;width:539px;height:176px;background:linear-gradient(135deg,#4b63a8,#7a8fd0 60%,#a5b3e0)}
.post-badge{left:114px;top:70px;width:310px;height:310px;border-radius:50%;background:var(--surface);border:4px solid var(--brand-mid);display:flex;align-items:center;justify-content:center}
.post-badge::before{content:"";position:absolute;inset:18px;border-radius:50%;border:2px solid var(--brand-mid)}
.post-badge span{font-size:40px;font-weight:700;color:var(--brand-mid)}
.post .actions{left:0;top:403px;width:539px;height:31px;border-top:1px solid #dadde1;display:flex;justify-content:space-around;align-items:center;font-size:12px;color:var(--muted)}
.post .actions span{display:flex;align-items:center;gap:6px}
</style>
</head>
<body>
<main class="page">

  <section class="cover abs">
    <div class="cover-wave abs" role="img" aria-label="Soft blue to cyan background band"></div>
    <div class="cover-dots-top abs" role="img" aria-label="Dot pattern decoration"></div>
    <div class="cover-dots-bottom abs" role="img" aria-label="Dot pattern decoration"></div>
    <div class="cover-illustration abs" role="img" aria-label="Illustration of a small team building a website layout on a large browser window"></div>
    <div class="cover-brand abs"><span class="mark"></span><span class="name">LumoCrest</span></div>
    <ul class="services abs">
      <li>Web Design and Development</li>
      <li>Search Engine Optimization</li>
      <li>Graphic Design</li>
      <li>Digital Marketing Services.</li>
    </ul>
  </section>

  <section class="identity abs">
    <div class="avatar abs"><span>LumoCrest</span></div>
    <h1 class="page-name abs">LumoCrest</h1>
    <p class="page-handle abs">@lumocrest.design · Digital Creator</p>
    <div class="call-btn abs">
      <svg width="14" height="14" viewBox="0 0 24 24"><path fill="#fff" d="M6.6 10.8a15 15 0 0 0 6.6 6.6l2.2-2.2c.3-.3.7-.4 1-.2 1.1.4 2.3.6 3.6.6.6 0 1 .4 1 1V20c0 .6-.4 1-1 1C10.6 21 3 13.4 3 4c0-.6.4-1 1-1h3.5c.6 0 1 .4 1 1 0 1.3.2 2.5.6 3.6.1.3 0 .7-.2 1z"/></svg>
      Call Now
    </div>
    <div class="divider abs"></div>
    <nav class="tabs abs">
      <a class="active">Home</a><a>Services</a><a>Reviews</a><a>Photos</a><a>More<span class="caret"></span></a>
    </nav>
    <div class="page-btn btn-like abs">
      <svg width="13" height="13" viewBox="0 0 24 24"><path fill="currentColor" d="M2 10h4v12H2zM8 22h10a2 2 0 0 0 2-1.6l1.5-8A2 2 0 0 0 19.5 10H14l1-5a2 2 0 0 0-3.6-1.4L8 9z"/></svg>Like
    </div>
    <div class="page-btn btn-message abs"><span class="dot-icon"></span>Message</div>
    <div class="page-btn btn-search abs">
      <svg width="13" height="13" viewBox="0 0 24 24"><circle cx="10" cy="10" r="7" fill="none" stroke="#1c1e21" stroke-width="2.5"/><path d="M15 15l6 6" stroke="#1c1e21" stroke-width="2.5"/></svg>
    </div>
    <div class="page-btn btn-more abs">•••</div>
  </section>

  <section class="card about abs">
    <h2>About</h2><span class="see-all">See All</span>
    <ul class="about-list">
      <li><span class="ico"><svg width="12" height="15" viewBox="0 0 12 16"><path fill="#8a8d91" d="M6 0a6 6 0 0 0-6 6c0 4.5 6 10 6 10s6-5.5 6-10a6 6 0 0 0-6-6zm0 8.5A2.5 2.5 0 1 1 6 3.5a2.5 2.5 0 0 1 0 5z"/></svg></span><span class="lnk">48 Harbor Lane #210 10001</span></li>
      <li><span class="ico"><svg width="15" height="15" viewBox="0 0 16 16"><circle cx="8" cy="8" r="8" fill="#8a8d91"/><rect x="7" y="7" width="2" height="5" fill="#fff"/><circle cx="8" cy="4.6" r="1.1" fill="#fff"/></svg></span><span class="desc">LumoCrest provides Web Design and Development, Search Engine Optimization, Graphic Design, and Digital Marketing Services.</span></li>
      <li><span class="ico"><svg width="15" height="15" viewBox="0 0 24 24"><path fill="#8a8d91" d="M2 10h4v12H2zM8 22h10a2 2 0 0 0 2-1.6l1.5-8A2 2 0 0 0 19.5 10H14l1-5a2 2 0 0 0-3.6-1.4L8 9z"/></svg></span><span>27 people like this</span></li>
      <li><span class="ico"><svg width="15" height="15" viewBox="0 0 16 16"><rect x="0" y="1" width="16" height="15" rx="2" fill="#8a8d91"/><path d="M4 9l3 3 5-6" stroke="#fff" stroke-width="1.8" fill="none"/></svg></span><span>28 people follow this</span></li>
      <li><span class="ico"><svg width="14" height="14" viewBox="0 0 24 24"><path fill="#8a8d91" d="M6.6 10.8a15 15 0 0 0 6.6 6.6l2.2-2.2c.3-.3.7-.4 1-.2 1.1.4 2.3.6 3.6.6.6 0 1 .4 1 1V20c0 .6-.4 1-1 1C10.6 21 3 13.4 3 4c0-.6.4-1 1-1h3.5c.6 0 1 .4 1 1 0 1.3.2 2.5.6 3.6.1.3 0 .7-.2 1z"/></svg></span><span>+1 555-014-0199</span></li>
      <li><span class="ico"><svg width="15" height="15" viewBox="0 0 16 16"><circle cx="8" cy="8" r="8" fill="#8a8d91"/></svg></span><span class="lnk">Send Message</span></li>
      <li><span class="ico"><svg width="15" height="12" viewBox="0 0 16 12"><rect width="16" height="12" rx="1" fill="#8a8d91"/><path d="M1 1l7 6 7-6" stroke="#fff" stroke-width="1.4" fill="none"/></svg></span><span class="lnk">mara@lumocrest.example</span></li>
      <li><span class="ico"><svg width="15" height="15" viewBox="0 0 16 16"><circle cx="8" cy="8" r="8" fill="#8a8d91"/><path d="M8 3.5V8l3 2" stroke="#fff" stroke-width="1.6" fill="none"/></svg></span><span class="open">Always Open</span></li>
      <li><span class="ico"><svg width="15" height="13" viewBox="0 0 16 14"><path fill="#8a8d91" d="M0 2h6l1.5 2H16v10H0z"/></svg></span><span class="lnk">Digital Creator · Web Designer</span></li>
    </ul>
  </section>

  <section class="card suggest abs">
    <h2>Suggest Edits</h2>
    <p>Is this the right phone number for this place?</p>
    <div class="field">+15550140199</div>
    <div class="choices"><span>Yes</span><span>Unsure</span><span>No</span></div>
  </section>

  <section class="card photos abs">
    <h2>Photos</h2><span class="see-all">See All</span>
  </section>

  <section class="card composer abs">
    <div class="me abs" role="img" aria-label="Viewer profile photo"></div>
    <div class="field abs">Create Post</div>
    <div class="tools abs">
      <span><svg width="15" height="14" viewBox="0 0 16 14"><rect width="16" height="14" rx="2" fill="#45bd62"/><path d="M2 12l4-5 3 3 2-2 3 4z" fill="#fff"/></svg>Photo/Video</span>
      <span><svg width="12" height="15" viewBox="0 0 12 16"><path fill="#e0414b" d="M6 0a6 6 0 0 0-6 6c0 4.5 6 10 6 10s6-5.5 6-10a6 6 0 0 0-6-6zm0 8.5A2.5 2.5 0 1 1 6 3.5a2.5 2.5 0 0 1 0 5z"/></svg>Check in</span>
      <span><svg width="16" height="14" viewBox="0 0 18 14"><circle cx="6" cy="4" r="3" fill="#1877f2"/><path d="M0 14c0-4 3-6 6-6s6 2 6 6z" fill="#1877f2"/><circle cx="13" cy="4" r="2.5" fill="#1877f2"/><path d="M12 8c3 0 6 2 6 6h-5c0-2-1-4-2-5z" fill="#1877f2"/></svg>Tag Friends</span>
    </div>
  </section>

  <article class="card post abs">
    <div class="author-mark abs"></div>
    <p class="headline abs"><b>LumoCrest</b> updated their profile picture.</p>
    <p class="time abs">10h · ◎</p>
    <span class="menu abs">•••</span>
    <div class="post-photo abs" role="img" aria-label="Blue-tinted photo of an office workspace behind the profile picture"></div>
    <div class="post-badge abs"><span>LumoCrest</span></div>
    <div class="actions abs">
      <span><svg width="14" height="14" viewBox="0 0 24 24"><path fill="none" stroke="#65676b" stroke-width="2" d="M2 10h4v12H2zM8 22h10a2 2 0 0 0 2-1.6l1.5-8A2 2 0 0 0 19.5 10H14l1-5a2 2 0 0 0-3.6-1.4L8 9z"/></svg>Like</span>
      <span><svg width="14" height="14" viewBox="0 0 24 24"><path fill="none" stroke="#65676b" stroke-width="2" d="M3 3h18v14H9l-5 4v-4H3z"/></svg>Comment</span>
      <span><svg width="14" height="14" viewBox="0 0 24 24"><path fill="none" stroke="#65676b" stroke-width="2" d="M14 4l8 7-8 7v-4c-6 0-10 2-12 6 0-7 4-12 12-12z"/></svg>Share</span>
    </div>
  </article>

</main>
</body>
</html>
```